Brightfern Couples Unity Program

We need a flyer that invites low-income Spanish speaking individuals to our program. The program is 12 weeks. We offer healthy relationship education, and financial stability. We also touch on workforce development. These workshops are for couples only.

We are in five locations, so we need a flyer that we can change the text to be able to update the address, dates and any additional information based on our needs.

Attached is the logo we would like to use. I have also attached a previous flyer that we created to give you an idea of the text that is included.

Target Market(s)

We are reaching out to low income adult couples

Font styles to use
Serif

Requirements
Must have
• This flyer must catch the eye of couples wanting to improve their relationship, and finances.
Nice to have
• Some space for us to plug in dates location and times. This flyer also has to have our funding statement at the bottom.

```html
<!DOCTYPE html>
<html lang="es">
<head>
<meta charset="utf-8">
<title>Talleres Para Parejas — Brightfern Couples Unity Program</title>
<link rel="stylesheet" href="https://fonts.googleapis.com/css2?family=Libre+Baskerville:wght@400;700&family=Montserrat:wght@600;700&family=Questrial&display=swap">
<style>
  :root {
    --orange: #f7941d;
    --navy: #0b3a66;
    --ink: #333333;
    --sky: #3a9ad9;
    --paper: #f4f4f4;
    --white: #ffffff;
  }
  * { box-sizing: border-box; margin: 0; padding: 0; }
  html, body { width: 927px; height: 1200px; overflow: hidden; background: var(--white); }
  .flyer {
    position: relative;
    width: 927px;
    height: 1200px;
    overflow: hidden;
    font-family: "Questrial", "Century Gothic", sans-serif;
    background: var(--paper);
  }

  /* Header */
  .brand {
    position: absolute;
    top: 40px; left: 0; width: 927px;
    text-align: center;
  }
  .brand-mark {
    display: block;
    width: 58px; height: 58px;
    margin: 0 auto 22px;
    border-radius: 50%;
    background: var(--orange);
  }
  .brand-name {
    font-family: "Questrial", sans-serif;
    font-size: 33px;
    color: var(--orange);
    letter-spacing: 0.2px;
  }
  .brand-tagline {
    width: 440px;
    margin: 8px auto 0;
    padding-top: 6px;
    border-top: 1.5px solid var(--navy);
    font-family: "Libre Baskerville", serif;
    font-weight: 700;
    font-size: 13px;
    line-height: 1.35;
    color: var(--navy);
    letter-spacing: 0.6px;
    font-variant: small-caps;
  }
  .title {
    position: absolute;
    top: 222px; left: 0; width: 927px;
    text-align: center;
    font-family: "Libre Baskerville", serif;
    font-weight: 700;
    font-size: 72px;
    color: var(--ink);
    letter-spacing: 1px;
  }
  .subtitle {
    position: absolute;
    top: 302px; left: 0; width: 927px;
    text-align: center;
    font-size: 29px;
    color: var(--ink);
  }

  /* Photo area */
  .photo {
    position: absolute;
    top: 345px; left: 0;
    width: 927px; height: 677px;
    background:
      radial-gradient(ellipse at 70% 45%, #d9a55a 0%, rgba(185,120,50,0.7) 30%, rgba(0,0,0,0) 60%),
      linear-gradient(100deg, #3b2e1c 0%, #5a4526 35%, #8a6431 60%, #b98446 80%, #6f4a24 100%);
  }
  .swoosh {
    position: absolute;
    top: 343px; left: 0;
    width: 927px; height: 130px;
  }

  /* Details */
  .details {
    position: absolute;
    left: 60px; top: 478px;
    color: var(--white);
  }
  .topics-heading {
    font-family: "Montserrat", sans-serif;
    font-weight: 700;
    font-size: 16px;
    color: var(--sky);
    margin-bottom: 4px;
  }
  .topics { list-style: none; }
  .topics li {
    position: relative;
    padding-left: 22px;
    font-size: 16.5px;
    line-height: 21px;
  }
  .topics li svg {
    position: absolute;
    left: 0; top: 4px;
    width: 14px; height: 14px;
  }
  .label {
    font-family: "Montserrat", sans-serif;
    font-weight: 700;
    color: var(--orange);
  }
  .dates-label { font-size: 31px; margin-top: 30px; line-height: 1.1; }
  .dates { font-size: 27px; margin-top: 2px; }
  .time-label { font-size: 31px; margin-top: 14px; line-height: 1.1; }
  .time { font-size: 27px; margin-top: 2px; }
  .place-label { font-size: 19px; margin-top: 16px; }
  .place { font-size: 16px; line-height: 22px; margin-top: 4px; }
  .note { font-size: 13px; color: var(--sky); margin-top: 10px; }

  /* Footer */
  .footer {
    position: absolute;
    top: 1022px; left: 0;
    width: 927px; height: 178px;
    background: var(--white);
  }
  .register {
    position: absolute;
    left: 60px; top: 26px;
    color: var(--ink);
  }
  .register-call {
    font-family: "Montserrat", sans-serif;
    font-weight: 700;
    font-size: 16.5px;
    color: var(--navy);
    margin-bottom: 4px;
  }
  .register-info { font-size: 16px; line-height: 20px; }
  .partners {
    position: absolute;
    right: 40px; top: 28px;
    display: flex; gap: 26px; align-items: center;
  }
  .partner {
    display: flex; align-items: center; gap: 8px;
    width: 170px;
    font-size: 14px; line-height: 17px;
    color: var(--orange);
  }
  .partner--second { color: #a3243b; width: 140px; }
  .partner-dot { flex: none; width: 26px; height: 26px; border-radius: 50%; background: currentColor; }
  .funding {
    position: absolute;
    left: 40px; right: 40px; top: 134px;
    font-size: 11.5px;
    line-height: 14px;
    color: var(--ink);
    text-align: center;
  }
</style>
</head>
<body>
<main class="flyer">

  <header class="brand">
    <span class="brand-mark"></span>
    <div class="brand-name">Brightfern Couples Unity Program</div>
    <div class="brand-tagline">Fortalecimiento de Relaciones | Capacitación Financiera<br>y Preparación Laboral</div>
  </header>

  <h1 class="title">Talleres Para Parejas</h1>
  <p class="subtitle">Porque una relación sana esta &nbsp;“A Nuestro Alcance”</p>

  <div class="photo" role="img" aria-label="Photograph of a couple embracing outdoors in warm autumn light"></div>

  <svg class="swoosh" viewBox="0 0 927 130" preserveAspectRatio="none" aria-hidden="true">
    <path d="M0 0 H927 V18 C640 6 300 26 0 92 Z" fill="var(--white)"/>
    <path d="M0 92 C300 26 640 6 927 18 V34 C640 20 300 38 0 100 Z" fill="var(--orange)"/>
    <path d="M0 100 C300 38 640 20 927 34 V100 C640 58 300 62 0 122 Z" fill="var(--navy)"/>
  </svg>

  <section class="details">
    <h2 class="topics-heading">Temas incluyen:</h2>
    <ul class="topics">
      <li><svg viewBox="0 0 14 14"><circle cx="7" cy="7" r="6" fill="none" stroke="#fff" stroke-width="1.2"/><path d="M4 7.2 L6.2 9.3 L10.2 4.8" fill="none" stroke="#fff" stroke-width="1.3"/></svg>Llaves para la buena &nbsp;communicación</li>
      <li><svg viewBox="0 0 14 14"><circle cx="7" cy="7" r="6" fill="none" stroke="#fff" stroke-width="1.2"/><path d="M4 7.2 L6.2 9.3 L10.2 4.8" fill="none" stroke="#fff" stroke-width="1.3"/></svg>Tipos de personalidad y expectativas</li>
      <li><svg viewBox="0 0 14 14"><circle cx="7" cy="7" r="6" fill="none" stroke="#fff" stroke-width="1.2"/><path d="M4 7.2 L6.2 9.3 L10.2 4.8" fill="none" stroke="#fff" stroke-width="1.3"/></svg>Señales de peligro en una relación</li>
      <li><svg viewBox="0 0 14 14"><circle cx="7" cy="7" r="6" fill="none" stroke="#fff" stroke-width="1.2"/><path d="M4 7.2 L6.2 9.3 L10.2 4.8" fill="none" stroke="#fff" stroke-width="1.3"/></svg>Técnicas para formar y &nbsp;sostener una relación sana</li>
      <li><svg viewBox="0 0 14 14"><circle cx="7" cy="7" r="6" fill="none" stroke="#fff" stroke-width="1.2"/><path d="M4 7.2 L6.2 9.3 L10.2 4.8" fill="none" stroke="#fff" stroke-width="1.3"/></svg>Resolucion de problemas</li>
      <li><svg viewBox="0 0 14 14"><circle cx="7" cy="7" r="6" fill="none" stroke="#fff" stroke-width="1.2"/><path d="M4 7.2 L6.2 9.3 L10.2 4.8" fill="none" stroke="#fff" stroke-width="1.3"/></svg>Como mantener la diversion</li>
      <li><svg viewBox="0 0 14 14"><circle cx="7" cy="7" r="6" fill="none" stroke="#fff" stroke-width="1.2"/><path d="M4 7.2 L6.2 9.3 L10.2 4.8" fill="none" stroke="#fff" stroke-width="1.3"/></svg>Como adminstrar el dinero entre<br>pareja Y muchos mas</li>
    </ul>

    <h2 class="label dates-label">Fecha de talleres</h2>
    <p class="dates">jueves octubre 03, 12, 19, 26</p>

    <h2 class="label time-label">Horario</h2>
    <p class="time">5:30pm –8:00pm</p>

    <h2 class="label place-label">Ubicación</h2>
    <p class="place">Willowbend Family Resource Center<br>2750 Larkspur Ave, Fairmont CA 90210<br>(555) 214-0386</p>

    <p class="note">*Cuidado de niños y cena será proporcionado</p>
  </section>

  <footer class="footer">
    <div class="register">
      <p class="register-call">Registración requerida &nbsp;Llámanos hoy!</p>
      <p class="register-info">Para más información llame a<br>Willowbend Family Resource Center<br>(555) 214-0391</p>
    </div>

    <div class="partners">
      <div class="partner"><span class="partner-dot"></span>Willowbend Family Resource Center</div>
      <div class="partner partner--second"><span class="partner-dot"></span>Harborline Community Partners</div>
    </div>

    <p class="funding">“Funding for this project was provided by the National Office for Family Services, Division of Children and Families, Grant: #12FS3456. &nbsp;These services are available to all eligible persons, regardless of race, gender, age, disability, or religion.”</p>
  </footer>

</main>
</body>
</html>
```